Q & Q Fabrications HVAC Mechanical Contractor Business Card

We need a business card for a HVAC/Plumbing Mechanical Contractor. Our website is http://www.qqfabrications-example.com. We would like to include the picture of the person on the card. Pictures of people for mock-ups can be found on our website. The blue on our logo is our primary color. We'd like this to be bold yet professional without too many colors but with some color to make sure it stands out.

Industry/Entity Type

Business

Contact Information for Business Card

Font styles to use
Sans Serif

Colors
000000

Requirements
Must have
• Our logo
• Person's picture
• Company Name
• Company Phone
• Person's email address
• Person's phone number
Nice to have
• Company Address
Should not have
• Clip art

```html
<!DOCTYPE html>
<html lang="en">
<head>
<meta charset="utf-8">
<title>Q &amp; Q Fabrications – Business Card</title>
<link rel="stylesheet" href="https://fonts.googleapis.com/css2?family=Source+Sans+3:ital,wght@0,400;0,600;0,700;1,400&display=swap">
<style>
  :root {
    --brand-blue: #3f8fd2;
    --ink: #1f1f1f;
    --muted: #555a60;
    --paper: #ffffff;
    --stage: #e6e7e9;
    --photo-light: #d9dadc;
    --photo-dark: #3a3d42;
  }
  * { box-sizing: border-box; margin: 0; padding: 0; }
  html, body { width: 1200px; height: 900px; overflow: hidden; }
  body {
    background: var(--stage);
    font-family: "Source Sans 3", sans-serif;
    color: var(--ink);
    display: flex;
    align-items: center;
    justify-content: center;
    gap: 40px;
  }
  .card {
    position: relative;
    width: 540px;
    height: 309px;
    overflow: hidden;
    box-shadow: 0 10px 30px rgba(0,0,0,0.18);
  }

  /* Front: solid brand blue with centred mark area */
  .card-front { background: var(--brand-blue); display: flex; align-items: center; justify-content: center; }
  .front-mark { display: flex; align-items: center; gap: 12px; }
  .front-mark .mark-square { width: 30px; height: 30px; background: var(--paper); }
  .front-mark .mark-name { color: var(--paper); font-weight: 700; font-size: 30px; letter-spacing: 0.2px; }

  /* Back: contact details */
  .card-back { background: var(--paper); }
  .brand { position: absolute; left: 22px; top: 20px; display: flex; align-items: flex-start; gap: 12px; }
  .brand .mark-square { width: 40px; height: 40px; background: var(--brand-blue); }
  .brand-name { font-weight: 700; font-size: 23px; line-height: 1; color: var(--ink); margin-top: 2px; }
  .brand-tagline { font-style: italic; font-size: 15px; color: var(--muted); margin-top: 4px; }

  .person { position: absolute; right: 150px; top: 100px; text-align: right; line-height: 1.2; }
  .person-name { font-weight: 700; font-size: 18px; }
  .person-title { font-style: italic; font-size: 14px; color: var(--muted); }
  .contact-row { font-size: 14px; }

  .contact-labels { position: absolute; left: 396px; top: 136px; line-height: 1.2; font-size: 14px; font-weight: 700; color: var(--brand-blue); }
  .contact-labels span { display: block; }
  .contact-labels span + span { margin-top: 2px; }

  .office { position: absolute; left: 22px; top: 192px; font-size: 13.5px; line-height: 1.3; color: var(--ink); }
  .office .label { color: var(--brand-blue); font-weight: 700; }
  .office .fax { margin-left: 40px; }

  .web-band {
    position: absolute; left: 0; right: 0; bottom: 0; height: 58px;
    background: var(--brand-blue);
    display: flex; align-items: center; padding-left: 22px;
    color: var(--paper); font-size: 19px;
  }
  .web-band strong { font-weight: 700; }

  .portrait {
    position: absolute; right: 0; bottom: 0; width: 150px; height: 200px;
    background: linear-gradient(180deg, var(--photo-light) 0%, #b7a89a 45%, var(--photo-dark) 100%);
  }
</style>
</head>
<body>
  <section class="card card-front" aria-label="Business card front">
    <div class="front-mark">
      <span class="mark-square"></span>
      <span class="mark-name">Q &amp; Q Fabrications</span>
    </div>
  </section>

  <section class="card card-back" aria-label="Business card back">
    <header class="brand">
      <span class="mark-square"></span>
      <div>
        <div class="brand-name">Q &amp; Q Fabrications, Inc.</div>
        <div class="brand-tagline">Mechanical Contractor</div>
      </div>
    </header>

    <div class="person">
      <div class="person-name">Daniel Whitford</div>
      <div class="person-title">CEO / Project Manager</div>
      <div class="contact-row">dwhitford@qqfabrications-example.com</div>
      <div class="contact-row">555-214-0187</div>
    </div>
    <div class="contact-labels"><span>Email</span><span>Direct</span></div>

    <div class="office">
      <div>1470 Alder Works Lane, Fairview, WI 53999-0142</div>
      <div><span class="label">Office:</span> 555-214-0100 <span class="fax"><span class="label">Fax:</span> 555-214-0199</span></div>
    </div>

    <div class="web-band">www.<strong>qqfabrications-example</strong>.com</div>

    <div class="portrait" role="img" aria-label="Portrait photo of the project manager in a dark suit jacket"></div>
  </section>
</body>
</html>
```